Classic/Royal 5 Items Black coloured Stationery Design

Hello,
I'm looking for an Elegant Stationery set consists of 5 items as the following,
1- Letterhead
2- Business Card
3- Invoice
4- CD/DVD with their Envelope Design
5- Envelope
To let the project move ahead easily, I've included a folder consists many designs I liked from various design sites and it consists of,
1- Business card
2- Corporate Identity
3- Invoice
4- Miscellanies
Inside the first three folders, you will find a folder named "Recommended", it contains designs that I like so much and hoping to have a design like them.
The "Miscellanies" folder got some designs for Inspiration.
I'm waiting for some greats designs, a joomla template designer is a bonus for me as I will need him to design the website layer soon.
Due to upload problems at ArtHerdly, I've uploaded the folder in a .rar archive at multiple site and here is the link http://zup.qx/TRALVBNE .
Thank you
Update :- You can use this alternative download link from my Google drive to download the designs
https://files.plomwex.net/file/d/7Kq2ZpR4m8sVxT1nLw9cYb3HfJd5

```html
<!DOCTYPE html>
<html lang="en">
<head>
<meta charset="utf-8">
<title>Velour Stay Stationery</title>
<link href="https://fonts.googleapis.com/css2?family=Questrial&display=swap" rel="stylesheet">
<style>
  :root {
    --backdrop: #a9a9b1;
    --board: #2e2f34;
    --board-deep: #26272b;
    --board-edge: #1f2024;
    --paper: #ffffff;
    --paper-shade: #f2f2f4;
    --ink: #2c2d31;
    --ink-soft: #6a6b70;
    --silver: #d9d9dd;
    --silver-soft: #9c9da3;
  }
  * { box-sizing: border-box; margin: 0; padding: 0; }
  html, body { width: 1200px; height: 976px; overflow: hidden; }
  body {
    background: var(--backdrop);
    font-family: "Questrial", "Helvetica Neue", Arial, sans-serif;
    position: relative;
  }
  .piece { position: absolute; }

  /* Open folder */
  .folder-open {
    left: 134px; top: 308px; width: 851px; height: 585px;
    background: var(--board);
    box-shadow: 0 2px 6px rgba(0,0,0,.25);
  }
  .folder-open__fold {
    position: absolute; left: 426px; top: 0; width: 1px; height: 100%;
    background: var(--board-edge);
  }
  .folder-open__insert {
    position: absolute; left: 443px; top: 4px; width: 391px; height: 382px;
    background: var(--paper-shade);
  }
  .folder-open__pocket {
    position: absolute; bottom: 0; height: 208px;
    background: var(--board-deep);
    border-top: 1px solid var(--board-edge);
  }
  .folder-open__pocket--left { left: 0; width: 426px; }
  .folder-open__pocket--right { left: 427px; width: 424px; }
  .folder-open__tab {
    position: absolute; left: 750px; top: 594px; width: 26px; height: 26px;
    border-radius: 50%; background: var(--board-edge);
  }
  .folder-open__slot {
    position: absolute; left: 710px; top: 856px; width: 40px; height: 20px;
    border-radius: 20px 20px 0 0; background: var(--board-edge);
  }
  .folder-open__contact {
    position: absolute; right: 20px; top: 477px;
    color: var(--paper); font-size: 7.5px; line-height: 1.35; text-align: right;
  }
  .folder-open__contact b { font-weight: 400; color: var(--silver); }

  /* Folder cover */
  .folder-cover {
    left: 86px; top: 240px; width: 392px; height: 572px;
    background: var(--board);
    box-shadow: 2px 4px 10px rgba(0,0,0,.35);
    text-align: center; color: var(--silver);
  }
  .brand { display: flex; flex-direction: column; align-items: center; }
  .brand__mark { width: 48px; height: 48px; border: 2px solid currentColor; }
  .brand__name { font-size: 26px; line-height: 1; margin-top: 10px; letter-spacing: .5px; }
  .brand__tagline { font-size: 11px; margin-top: 6px; letter-spacing: .3px; }
  .folder-cover .brand { margin-top: 128px; }
  .folder-cover__rule {
    position: absolute; left: 130px; top: 508px; width: 140px; height: 3px;
    background: var(--silver-soft);
  }

  /* Letterhead */
  .letterhead {
    left: 686px; top: 62px; width: 316px; height: 571px;
    background: var(--paper); color: var(--ink);
    box-shadow: 0 2px 6px rgba(0,0,0,.2);
  }
  .letterhead .brand { margin-top: 28px; }
  .letterhead .brand__mark { width: 30px; height: 30px; border-width: 1.5px; }
  .letterhead .brand__name { font-size: 15px; margin-top: 6px; }
  .letterhead .brand__tagline { font-size: 7px; margin-top: 3px; color: var(--ink-soft); }
  .letterhead__footer {
    position: absolute; left: 86px; right: 22px; bottom: 16px;
    font-size: 5.5px; text-align: center; color: var(--ink-soft); line-height: 1.5;
  }
  .letterhead__footer b { color: var(--ink); }
  .letterhead__footer hr { border: 0; height: 2px; background: var(--ink); margin-top: 3px; }

  /* Compliment card */
  .compliment {
    left: 659px; top: 62px; width: 98px; height: 169px;
    background: var(--paper); color: var(--ink);
    box-shadow: 0 2px 5px rgba(0,0,0,.25);
  }
  .compliment .brand { margin-top: 14px; }
  .compliment .brand__mark { width: 18px; height: 18px; border-width: 1px; }
  .compliment .brand__name { font-size: 9px; margin-top: 4px; }
  .compliment .brand__tagline { font-size: 5px; margin-top: 2px; color: var(--ink-soft); }
  .compliment__address {
    position: absolute; left: 0; right: 0; bottom: 9px;
    font-size: 4.5px; text-align: center; line-height: 1.4; color: var(--ink-soft);
  }
  .compliment__address hr { border: 0; height: 1.5px; background: var(--ink); width: 40px; margin: 3px auto 0; }

  /* Business card */
  .business-card {
    left: 1019px; top: 715px; width: 67px; height: 169px;
    background: var(--board);
    box-shadow: 1px 3px 6px rgba(0,0,0,.35);
    color: var(--silver); text-align: center;
  }
  .business-card__name { font-size: 6.5px; margin-top: 25px; }
  .business-card__role { font-size: 4px; color: var(--silver-soft); margin-top: 1px; }
  .business-card__mark {
    width: 24px; height: 24px; border: 1px solid var(--silver-soft);
    margin: 24px auto 0; opacity: .5;
  }
  .business-card__contact {
    position: absolute; left: 12px; bottom: 12px;
    font-size: 3.8px; line-height: 1.45; text-align: left; color: var(--silver);
  }
  .business-card__contact hr { border: 0; height: 1px; background: var(--silver-soft); width: 40px; margin-top: 3px; }
</style>
</head>
<body>

  <section class="piece folder-open">
    <div class="folder-open__insert"></div>
    <div class="folder-open__pocket folder-open__pocket--left"></div>
    <div class="folder-open__pocket folder-open__pocket--right"></div>
    <div class="folder-open__fold"></div>
    <address class="folder-open__contact">
      4120 Harbor Lane<br>
      Coral Vale, FL 33010<br>
      <b>T:</b> +61 40210 5500<br>
      <b>E:</b> info@velourstay.com<br>
      www.velourstay.com
    </address>
  </section>
  <div class="piece folder-open__tab" style="left:884px;top:902px;display:none"></div>

  <section class="piece folder-cover">
    <div class="brand">
      <span class="brand__mark"></span>
      <span class="brand__name">Velour Stay</span>
      <span class="brand__tagline">Hotels and General Supplies</span>
    </div>
    <div class="folder-cover__rule"></div>
  </section>

  <section class="piece letterhead">
    <div class="brand">
      <span class="brand__mark"></span>
      <span class="brand__name">Velour Stay</span>
      <span class="brand__tagline">Hotels and General Supplies</span>
    </div>
    <footer class="letterhead__footer">
      4120 Harbor Lane, Coral Vale, FL 33010<br>
      <b>Tel:</b> +61 40210 5500 · <b>Email:</b> info@velourstay.com · <b>Web:</b> www.velourstay.com
      <hr>
    </footer>
  </section>

  <section class="piece compliment">
    <div class="brand">
      <span class="brand__mark"></span>
      <span class="brand__name">Velour Stay</span>
      <span class="brand__tagline">Hotels and General Supplies</span>
    </div>
    <address class="compliment__address">
      4120 Harbor Lane<br>
      Coral Vale, FL 33010<br>
      www.velourstay.com
      <hr>
    </address>
  </section>

  <section class="piece business-card">
    <p class="business-card__name">Marisol DENAVE</p>
    <p class="business-card__role">Managing Partner</p>
    <div class="business-card__mark"></div>
    <address class="business-card__contact">
      T: +61 40210 5500<br>
      M: +61 40210 5501<br>
      E: info@velourstay.com
      <hr>
    </address>
  </section>

</body>
</html>
```